Calder Pizza - Takeout Menu Design

We are looking for a takeout menu design.
We are looking for a( 5" x 8.5" DOUBLE SIDED) flyer with our available pizza flavors
Must be easy to ready and not "busy"

Must include our logo (attached)
website: www.calderpizza.ca
address:
Fenwick Ridge Plaza
417, 318 9 Avenue SW
and the following details:
Visit our website for our complete appetizer, pasta, salad and catering menu.

Winner of this contest will also be offered to create a few print designs via printhive.

Please do not hesitate to ask any questions.

Target Market(s)

Business / Office clientele

Industry/Entity Type

Pizza place / specializing in corporate orders

Requirements
Must have
• Easy to read
Should not have
• Can not be busy or cluttered

```html
<!DOCTYPE html>
<html lang="en">
<head>
<meta charset="utf-8">
<title>Calder Pizza – Specialty Take-Out Pizza</title>
<link href="https://fonts.googleapis.com/css2?family=Fjalla+One&family=Poppins:wght@400;500;600;700&display=swap" rel="stylesheet">
<style>
  :root {
    --paper: #f4f4f4;
    --paper-grain: #e6e6e6;
    --ink: #1d1d1d;
    --price: #c9362b;
    --rule: #e02a24;
    --band: #c22a1f;
    --band-dark: #a8231a;
    --white: #ffffff;
  }
  * { margin: 0; padding: 0; box-sizing: border-box; }
  html, body { width: 706px; height: 1200px; overflow: hidden; }
  body {
    font-family: "Poppins", sans-serif;
    color: var(--ink);
    background: var(--paper);
  }
  .menu {
    position: relative;
    width: 706px;
    height: 1200px;
    overflow: hidden;
    background: repeating-linear-gradient(90deg, var(--paper) 0 38px, var(--paper-grain) 38px 40px, var(--paper) 40px 71px);
  }
  .hero-food {
    position: absolute;
    left: -8px; top: -8px;
    width: 152px; height: 110px;
    border-radius: 0 0 80px 0;
    background: radial-gradient(circle at 32% 38%, #e8b15a 0%, #d98a3a 42%, #3f8a2c 72%, #cf2e22 100%);
  }
  .title {
    position: absolute;
    left: 151px; top: 42px;
    font-family: "Fjalla One", sans-serif;
    font-weight: 400;
    white-space: nowrap;
    color: var(--ink);
    line-height: 1;
  }
  .title .lead { font-size: 43px; letter-spacing: -0.5px; }
  .title .rest { font-size: 28px; letter-spacing: -0.2px; }
  .title-rule {
    position: absolute;
    left: 310px; top: 95px;
    width: 358px; height: 3px;
    background: var(--rule);
    border-radius: 2px;
  }
  .pizza-list { list-style: none; }
  .pizza {
    position: absolute;
    left: 54px; right: 50px;
    height: 34px;
  }
  .pizza-name { font-size: 14.5px; font-weight: 500; line-height: 16px; }
  .pizza-desc { font-size: 11.3px; line-height: 14px; }
  .pizza-desc.small { font-size: 9.6px; }
  .price {
    position: absolute;
    top: 0; right: 0;
    font-size: 14.5px; font-weight: 600;
    color: var(--price);
    white-space: nowrap;
    word-spacing: 6px;
  }
  .tax-note {
    position: absolute;
    right: 50px; top: 1041px;
    font-size: 14px; font-weight: 600;
    letter-spacing: 1.5px;
  }
  .footer-band { position: absolute; left: 0; top: 1040px; width: 706px; height: 160px; }
  .website {
    position: absolute;
    left: 55px; top: 1100px;
    font-size: 24px; font-weight: 700;
    letter-spacing: 1.8px;
    color: var(--white);
  }
  .address {
    position: absolute;
    left: 58px; top: 1131px;
    font-size: 16.5px; font-weight: 500;
    color: var(--white);
  }
  .social { position: absolute; left: 547px; top: 1116px; display: flex; gap: 8px; }
  .social span { width: 28px; height: 28px; border-radius: 50%; background: var(--white); }
</style>
</head>
<body>
<main class="menu">
  <div class="hero-food" role="img" aria-label="Pizza with tomato, mushrooms and green pepper"></div>
  <h1 class="title"><span class="lead">Specialty Take</span> <span class="rest">- Out Pizza - 8" &amp; 13"</span></h1>
  <div class="title-rule"></div>

  <ul class="pizza-list">
    <li class="pizza" style="top:110px"><p class="pizza-name">All Meat</p><p class="pizza-desc">Pepperoni, Beef &amp; Smoked Ham &amp; Bacon</p><span class="price">$12.99 $30.95</span></li>
    <li class="pizza" style="top:146px"><p class="pizza-name">Double Pepperoni</p><p class="pizza-desc">Loads of Pepperoni</p><span class="price">$13.49 $32.95</span></li>
    <li class="pizza" style="top:182px"><p class="pizza-name">Hot Honey Pepperoni</p><p class="pizza-desc">Double Pepperoni and drizzled with Hot Honey</p><span class="price">$14.49 $34.95</span></li>
    <li class="pizza" style="top:218px"><p class="pizza-name">Hawaiian Heat</p><p class="pizza-desc">Smoked Ham, Pineapple and Banana Peppers</p><span class="price">$13.49 $32.95</span></li>
    <li class="pizza" style="top:253px"><p class="pizza-name">Four Cheese</p><p class="pizza-desc">Mozzarella, Feta, Romano and Cheddar Cheese</p><span class="price">$13.49 $32.95</span></li>
    <li class="pizza" style="top:288px"><p class="pizza-name">Montreal</p><p class="pizza-desc">Pepperoni &amp; Double Smoked Bacon</p><span class="price">$13.49 $32.95</span></li>
    <li class="pizza" style="top:323px"><p class="pizza-name">Montreal Heat</p><p class="pizza-desc">Pepperoni, Double Smoked Bacon &amp; Banana Peppers</p><span class="price">$13.99 $33.95</span></li>
    <li class="pizza" style="top:359px"><p class="pizza-name">Supreme</p><p class="pizza-desc">Pepperoni, Mushrooms &amp; Green Peppers</p><span class="price">$13.49 $32.95</span></li>
    <li class="pizza" style="top:394px"><p class="pizza-name">Canadian</p><p class="pizza-desc">Pepperoni, Mushrooms &amp; Ham</p><span class="price">$13.49 $32.95</span></li>
    <li class="pizza" style="top:430px"><p class="pizza-name">BBQ Chicken</p><p class="pizza-desc">Chicken Breast, Hickory BBQ Sauce &amp; Red Onions.</p><span class="price">$13.99 $33.95</span></li>
    <li class="pizza" style="top:467px"><p class="pizza-name">BBQ Chicken Plus</p><p class="pizza-desc">Chicken Breast, Hickory BBQ Sauce, Red Onions &amp; Cilantro</p><span class="price">$14.79 $34.95</span></li>
    <li class="pizza" style="top:502px"><p class="pizza-name">Spicy BBQ Chicken</p><p class="pizza-desc">Chicken Breast, Hickory BBQ Sauce, Red Onions &amp; Banana Peppers</p><span class="price">$14.49 $35.95</span></li>
    <li class="pizza" style="top:538px"><p class="pizza-name">Sweet Chili Chicken</p><p class="pizza-desc">Chicken Breast, Pineapple, Red Onions &amp; Sweet Chili Sauce</p><span class="price">$14.49 $35.95</span></li>
    <li class="pizza" style="top:577px"><p class="pizza-name">Chicken Club</p><p class="pizza-desc">Chicken Breast, Pineapple, Red Onions &amp; Sweet Chili Sauce</p><span class="price">$14.79 $35.95</span></li>
    <li class="pizza" style="top:613px"><p class="pizza-name">Athenean</p><p class="pizza-desc">Chicken Breast, Spinach, Feta Cheese and Tomato</p><span class="price">$14.49 $34.95</span></li>
    <li class="pizza" style="top:650px"><p class="pizza-name">Greek Supreme</p><p class="pizza-desc">Chicken Breast, Feta Cheese, Tomato, Green Pepper, Red Onions &amp; Black Olives</p><span class="price">$14.99 $35.95</span></li>
    <li class="pizza" style="top:686px"><p class="pizza-name">Mediterranean Chicken</p><p class="pizza-desc">Seasoned Chicken Breast, Tomatoes, Red Onions and Feta Cheese</p><span class="price">$14.79 $35.95</span></li>
    <li class="pizza" style="top:722px"><p class="pizza-name">Original Spinach</p><p class="pizza-desc">Spinach &amp; Feta Cheese</p><span class="price">$13.49 $32.95</span></li>
    <li class="pizza" style="top:757px"><p class="pizza-name">Zeus</p><p class="pizza-desc">Spinach, Feta Cheese and Tomatoes</p><span class="price">$13.95 $33.95</span></li>
    <li class="pizza" style="top:793px"><p class="pizza-name">Greek</p><p class="pizza-desc">Feta Cheese, Tomato, Green Peppers, Red Onions and Black Olives</p><span class="price">$13.99 $33.95</span></li>
    <li class="pizza" style="top:829px"><p class="pizza-name">Vegetarian</p><p class="pizza-desc">Mushrooms, Tomatoes, Green Peppers and Black Olives</p><span class="price">$13.49 $32.95</span></li>
    <li class="pizza" style="top:868px"><p class="pizza-name">Veggie Delight</p><p class="pizza-desc">Mushrooms, Tomatoes, Green Peppers, Black Olives &amp; Onions</p><span class="price">$13.95 $33.95</span></li>
    <li class="pizza" style="top:904px"><p class="pizza-name">Deluxe</p><p class="pizza-desc">Pepperoni, Mushrooms, Ham, Tomatoes, Green Peppers and Red Onions</p><span class="price">$14.49 $34.95</span></li>
    <li class="pizza" style="top:940px"><p class="pizza-name">Calder Special</p><p class="pizza-desc">Pepperoni, Mushrooms, Ham, Green Peppers and Black Olives</p><span class="price">$14.49 $34.95</span></li>
    <li class="pizza" style="top:979px"><p class="pizza-name">Dill Pickle</p><p class="pizza-desc small">Crispy Dill Pickles, Fresh Dill with our cream based garlic sauce. Served with our without bacon.</p><span class="price">$13.49 $32.95 / $14.49 $35.95</span></li>
    <li class="pizza" style="top:1015px"><p class="pizza-name">BBQ Pulled Pork</p><p class="pizza-desc">Pulled Pork, Red Onions, Red Peppers and Cilantro.</p><span class="price">$14.49 $35.95</span></li>
  </ul>

  <p class="tax-note">GST not included</p>

  <svg class="footer-band" viewBox="0 0 706 160" aria-hidden="true">
    <path d="M0 76 L40 70 L80 60 L120 52 L150 44 L175 46 L200 34 L225 30 L250 22 L280 18 L310 16 L340 12 L365 8 L385 6 L400 16 L420 18 L440 36 L462 54 L490 50 L520 44 L550 40 L580 34 L610 30 L640 28 L670 22 L706 18 L706 160 L0 160 Z" fill="var(--band)"/>
    <path d="M0 125 L706 100 L706 160 L0 160 Z" fill="var(--band-dark)" opacity="0.2"/>
  </svg>

  <p class="website">www.calderpizza.ca</p>
  <p class="address">Fenwick Ridge Plaza 417, 318 9 Avenue SW</p>
  <div class="social" aria-hidden="true"><span></span><span></span><span></span></div>
</main>
</body>
</html>
```